Candid Dialogues about Mental Health

I would like a website designed that would be used to upload podcasts, videos and written material about mental health. Where people will be being as honest, open and truthful as they can about mental health issues.
I would like it to look calming and soothing. Inspired by Pellard's paintings and colour schemes.

I am on WorkNexo as Dr Hannah Westcott - and quillet as drhannahwestcott

Target Market(s)

Healthcare professionals and users of services who want to think at a deeper level about the nature of mental illness

Number of Pages Required

1 page

```html
<!DOCTYPE html>
<html lang="en">
<head>
<meta charset="utf-8">
<title>Candid Dialogues about Mental Health</title>
<link href="https://fonts.googleapis.com/css2?family=Josefin+Sans:wght@300;400;600&family=Poppins:wght@300;400;500;600&family=Roboto+Slab:wght@700&display=swap" rel="stylesheet">
<style>
:root{
  --paper:#efece7;
  --sage:#b3c3c1;
  --sage-panel:#a9b9b5;
  --teal-dark:#5c7a78;
  --teal-ink:#4f6b69;
  --forest:#2f4a2a;
  --slate:#4e5b5a;
  --text:#6f6f6f;
  --text-dark:#4a4a4a;
  --line:#d9d5cf;
  --white:#ffffff;
  --mint:#5fd3c6;
}
*{box-sizing:border-box;margin:0;padding:0}
html,body{width:1200px;height:3736px;overflow:hidden}
body{position:relative;background:var(--paper);font-family:'Poppins',sans-serif;color:var(--text)}
section,header,footer{position:absolute;left:0;width:1200px}
a{text-decoration:none;color:inherit}

/* header */
.site-header{top:0;height:91px;border-bottom:1px solid var(--line)}
.brand{position:absolute;display:flex;align-items:center;gap:8px;font-family:'Josefin Sans',sans-serif;font-weight:600;font-size:16px;color:var(--forest)}
.brand-dot{width:14px;height:14px;border-radius:50%;background:currentColor}
.site-header .brand{left:232px;top:31px}
.main-nav a{position:absolute;top:34px;font-size:14px;color:var(--teal-ink);line-height:20px}

/* hero */
.hero{top:0;height:731px}
.photo{position:absolute}
.hero-panel{position:absolute;left:573px;top:151px;width:285px;height:382px;background:var(--sage-panel);box-shadow:0 10px 24px rgba(0,0,0,.18);padding:64px 24px 0 24px;color:var(--white)}
.hero-title{font-family:'Josefin Sans',sans-serif;font-weight:300;font-size:40px;line-height:46px}
.hero-copy{margin-top:20px;font-size:11.5px;line-height:21px;font-weight:300}
.btn-explore{position:absolute;left:26px;top:323px;width:106px;height:34px;background:var(--forest);color:var(--white);font-size:12px;display:flex;align-items:center;justify-content:center;gap:6px}

/* section heads */
.section-title{position:absolute;left:231px;font-family:'Josefin Sans',sans-serif;font-weight:300;font-size:37px;line-height:44px;letter-spacing:12px}
.rule{position:absolute;height:1px}
.btn{position:absolute;display:flex;align-items:center;justify-content:center;font-size:11.5px}
.btn-light{background:var(--paper);color:var(--text)}
.btn-dark{background:var(--teal-dark);color:var(--white)}

/* podcasts */
.podcasts{top:731px;height:601px;background:var(--sage);overflow:hidden}
.podcasts .section-title{top:38px;color:var(--white)}
.podcasts .rule{left:500px;top:60px;width:314px;background:var(--white)}
.section-lede{position:absolute;left:231px;top:86px;font-size:12px;line-height:19px;color:var(--white);font-weight:300}
.podcast-card{position:absolute;top:154px;width:237px;height:344px;background:var(--paper);overflow:hidden}
.podcast-art{position:absolute;left:0;top:0;width:237px;height:224px}
.play-ring{position:absolute;left:10px;top:18px}
.art-title{position:absolute;left:16px;bottom:134px;font-family:'Roboto Slab',serif;font-weight:700;color:var(--white);font-size:27px;line-height:36px;letter-spacing:1px}
.art-title.small{font-size:19px;line-height:23px}
.card-meta{position:absolute;left:15px;right:15px;top:230px;display:flex;justify-content:space-between;font-size:10.5px;color:#9a9a9a}
.card-text{position:absolute;left:15px;right:14px;top:258px;font-size:11.5px;line-height:19px;color:var(--text-dark)}
.card-more{position:absolute;left:15px;top:316px;font-size:10px;color:var(--text-dark)}
.edge-fade{position:absolute;top:154px;height:344px}
.carousel-arrow{position:absolute}

/* videos */
.videos{top:1332px;height:1019px}
.videos .section-title{top:107px;color:var(--teal-ink)}
.videos .rule{left:424px;top:129px;width:374px;background:var(--teal-ink)}
.video-thumb{position:absolute;width:312px;height:170px}
.video-thumb svg{position:absolute;left:123px;top:52px}
.video-name{position:absolute;font-family:'Josefin Sans',sans-serif;font-weight:600;font-size:28px;line-height:34px;letter-spacing:2.5px;color:var(--teal-ink)}
.video-copy{position:absolute;font-size:12px;line-height:19px;color:var(--text-dark);width:270px}
.learn-more{position:absolute;font-size:11.5px;font-weight:600;color:var(--teal-ink);line-height:20px}
.also{position:absolute;font-size:11.5px;color:#9a9a9a;line-height:20px}
.also b{color:var(--teal-ink);font-weight:600}
.divider{position:absolute;left:231px;width:737px;height:1px;background:var(--line)}

/* articles */
.articles{top:2351px;height:499px;background:var(--sage)}
.articles .section-title{top:75px;color:var(--white)}
.articles .rule{left:469px;top:97px;width:373px;background:var(--white)}
.feature-card{position:absolute;left:231px;top:148px;width:335px;height:251px}
.feature-overlay{position:absolute;left:0;top:151px;width:335px;height:100px;background:rgba(90,114,114,.92);color:var(--white);padding:0 11px}
.read-time{position:absolute;font-size:9px;color:var(--white)}
.feature-title{position:absolute;left:11px;top:14px;font-size:12px;font-weight:600}
.feature-date{position:absolute;left:11px;top:32px;font-size:8px;opacity:.85}
.feature-copy{position:absolute;left:11px;top:50px;width:300px;font-size:10px;line-height:16px}
.side-card{position:absolute;left:582px;width:386px;height:116px;background:var(--paper)}
.side-thumb{position:absolute;left:0;top:0;width:128px;height:116px}
.side-title{position:absolute;left:146px;width:225px;font-size:12px;line-height:16px;font-weight:600;color:var(--teal-ink)}
.side-date{position:absolute;left:146px;font-size:8px;color:#9a9a9a}
.side-copy{position:absolute;left:146px;width:226px;font-size:9.5px;line-height:16px;color:var(--text-dark)}

/* newsletter */
.newsletter{top:2850px;height:230px}
.news-title{position:absolute;left:0;width:1200px;top:54px;text-align:center;font-family:'Josefin Sans',sans-serif;font-weight:300;font-size:25px;line-height:30px;letter-spacing:3px;color:#6c7474}
.news-lede{position:absolute;left:0;width:1200px;top:100px;text-align:center;font-size:12px;color:var(--text-dark)}
.email-field{position:absolute;left:354px;top:136px;width:364px;height:34px;background:rgba(239,236,231,.85);color:#c9c5bf;font-size:12px;padding:7px 12px}
.newsletter .btn{left:718px;top:136px;width:125px;height:34px;font-weight:600;font-size:13px}

/* contact */
.contact{top:3080px;height:445px}
.contact-title{position:absolute;left:601px;top:66px;font-family:'Josefin Sans',sans-serif;font-weight:300;font-size:27px;line-height:32px;letter-spacing:3px;color:#6c7474}
.contact-lede{position:absolute;left:601px;top:109px;width:350px;font-size:12px;line-height:18px;color:var(--text-dark)}
.field{position:absolute;left:601px;width:294px;border:1px solid var(--line);background:#f4f2ee;font-size:10.5px;color:#a9a6a1;padding:7px 13px}
.contact .btn{left:601px;top:365px;width:100px;height:30px;font-weight:600;font-size:12.5px}

/* footer */
.site-footer{top:3525px;height:211px;background:var(--slate);color:var(--white)}
.site-footer .brand{left:232px;top:78px;color:var(--white)}
.footer-nav a{position:absolute;top:77px;font-size:14.5px;font-weight:500;line-height:22px}
.social{position:absolute;right:232px;top:81px;display:flex;gap:9px;font-size:10px;line-height:18px;color:#d7dedd;white-space:nowrap}
.site-footer .rule{left:231px;top:182px;width:737px;background:#7f8b8a}
.footer-url{position:absolute;left:0;width:1200px;top:190px;text-align:center;font-size:10px;color:#d7dedd}
</style>
</head>
<body>

<header class="site-header">
  <a class="brand" href="#"><span class="brand-dot"></span>Candid Dialogues</a>
  <nav class="main-nav">
    <a href="#" style="left:571px">Home</a>
    <a href="#" style="left:655px">Podcasts</a>
    <a href="#" style="left:758px">Blog</a>
    <a href="#" style="left:831px">About</a>
    <a href="#" style="left:915px">Contact</a>
  </nav>
</header>

<section class="hero">
  <div class="photo" role="img" aria-label="Woman speaking into a handheld microphone against a red curtain" style="left:0;top:131px;width:237px;height:455px;background:linear-gradient(160deg,#6a1e22 0%,#3a1416 45%,#1c1a1a 100%)"></div>
  <div class="photo" role="img" aria-label="Smiling man in headphones recording a podcast at a desk with a laptop" style="left:280px;top:91px;width:398px;height:536px;background:linear-gradient(170deg,#7a6f63 0%,#a8a198 40%,#c9c2ba 75%,#8d8882 100%)"></div>
  <div class="hero-panel">
    <h1 class="hero-title">Candid<br>Dialogues</h1>
    <p class="hero-copy">Elevating awareness around suicide, depression and mental wellness. Explore our podcasts and candid interviews with many individuals who share their experiences in an open and honest way.</p>
    <a class="btn-explore" href="#">Explore
      <svg width="8" height="10" viewBox="0 0 8 10"><path d="M2 1l4 4-4 4" fill="none" stroke="#fff" stroke-width="1.3"/></svg></a>
  </div>
  <div class="photo" role="img" aria-label="Woman in headphones laughing while speaking into a studio microphone" style="left:891px;top:131px;width:309px;height:454px;background:linear-gradient(120deg,#c7cfd6 0%,#e6e1d9 45%,#d1b89a 80%,#b49777 100%)"></div>
</section>

<section class="podcasts">
  <h2 class="section-title">PODCASTS</h2>
  <div class="rule"></div>
  <a class="btn btn-light" href="#" style="left:831px;top:44px;width:162px;height:33px">Browse All Podcasts</a>
  <p class="section-lede">Explore our collection of podcasts on many<br>topics about mental health, updated weekly.</p>

  <article class="podcast-card" style="left:-19px">
    <div class="podcast-art" role="img" aria-label="Man in headphones speaking at a podcast microphone" style="background:linear-gradient(150deg,#3d4f6b,#6d7688 55%,#8c8c8e)"></div>
    <svg class="play-ring" width="22" height="22" viewBox="0 0 22 22"><circle cx="11" cy="11" r="9.5" fill="none" stroke="#5fd3c6" stroke-width="1.6"/><path d="M9 7l6 4-6 4z" fill="#5fd3c6"/></svg>
    <div class="art-title small">Prof. Marsfield<br>Interview –<br>Overcoming Suicide</div>
    <div class="card-meta"><span>Description</span><span>30 mins</span></div>
    <p class="card-text">Prof. Owen Marsfield talks about mental wellness at Millbrook prevention in this latest podcast</p>
    <span class="card-more">More ›</span>
  </article>

  <article class="podcast-card" style="left:231px">
    <div class="podcast-art" role="img" aria-label="Two women recording a podcast together with a headphone graphic" style="background:linear-gradient(150deg,#b9874e,#d6a56c 50%,#c79866)"></div>
    <svg class="play-ring" width="22" height="22" viewBox="0 0 22 22"><circle cx="11" cy="11" r="9.5" fill="none" stroke="#5fd3c6" stroke-width="1.6"/><path d="M9 7l6 4-6 4z" fill="#5fd3c6"/></svg>
    <div class="card-meta"><span>Description</span><span>45 mins</span></div>
    <p class="card-text">Tara Bellamy shares her journey overcoming her mental issues and opens up in this latest pod…</p>
    <span class="card-more">More ›</span>
  </article>

  <article class="podcast-card" style="left:480px">
    <div class="podcast-art" role="img" aria-label="Man in headphones in a neon-lit recording studio" style="background:linear-gradient(150deg,#4a2a5c,#7a3a5a 45%,#2c2540)"></div>
    <svg class="play-ring" width="22" height="22" viewBox="0 0 22 22"><circle cx="11" cy="11" r="9.5" fill="none" stroke="#5fd3c6" stroke-width="1.6"/><path d="M9 7l6 4-6 4z" fill="#5fd3c6"/></svg>
    <div class="art-title" style="letter-spacing:3px">Dr. Ellis</div>
    <div class="card-meta"><span>Description</span><span>15 mins</span></div>
    <p class="card-text">Dr. Ellis sits down with our new guest Callum for our September podcast. Topic of the day…</p>
    <span class="card-more">More ›</span>
  </article>

  <article class="podcast-card" style="left:730px">
    <div class="podcast-art" role="img" aria-label="Woman speaking into a studio microphone with a blue tint" style="background:linear-gradient(150deg,#1d3157,#27406b 50%,#1a2d4f)"></div>
    <svg class="play-ring" width="22" height="22" viewBox="0 0 22 22"><circle cx="11" cy="11" r="9.5" fill="none" stroke="#5fd3c6" stroke-width="1.6"/><path d="M9 7l6 4-6 4z" fill="#5fd3c6"/></svg>
    <div class="art-title">Today's<br>Talk On<br>Depression</div>
    <div class="card-meta"><span>Description</span><span>35 mins</span></div>
    <p class="card-text">Saturday Podcast with Rosa &amp; Jenna focuses on the stigma surrounding suicide survivors…</p>
    <span class="card-more">More ›</span>
  </article>

  <article class="podcast-card" style="left:979px">
    <div class="podcast-art" role="img" aria-label="Two people recording a podcast with a headphone graphic" style="background:linear-gradient(150deg,#3e5a78,#6f8aa2 55%,#9aa7b0)"></div>
    <svg class="play-ring" width="22" height="22" viewBox="0 0 22 22"><circle cx="11" cy="11" r="9.5" fill="none" stroke="#5fd3c6" stroke-width="1.6"/><path d="M9 7l6 4-6 4z" fill="#5fd3c6"/></svg>
    <div class="card-meta"><span>Description</span><span>40 mins</span></div>
    <p class="card-text">Tara Bellamy shares her journey overcoming her mental issues and opens up in this latest pod…</p>
    <span class="card-more">More ›</span>
  </article>

  <div class="edge-fade" style="left:0;width:230px;background:linear-gradient(90deg,rgba(179,195,193,.8),rgba(179,195,193,.25) 80%,rgba(179,195,193,0))"></div>
  <div class="edge-fade" style="left:979px;width:221px;background:linear-gradient(270deg,rgba(179,195,193,.85),rgba(179,195,193,.3) 70%,rgba(179,195,193,0))"></div>

  <svg class="carousel-arrow" style="left:555px;top:531px" width="30" height="30" viewBox="0 0 30 30"><circle cx="15" cy="15" r="13.5" fill="none" stroke="#fff" stroke-width="1.2"/><path d="M17 10l-5 5 5 5" fill="none" stroke="#fff" stroke-width="1.3"/></svg>
  <svg class="carousel-arrow" style="left:614px;top:531px" width="30" height="30" viewBox="0 0 30 30"><circle cx="15" cy="15" r="13.5" fill="none" stroke="#fff" stroke-width="1.2"/><path d="M13 10l5 5-5 5" fill="none" stroke="#fff" stroke-width="1.3"/></svg>
</section>

<section class="videos">
  <h2 class="section-title">VIDEOS</h2>
  <div class="rule"></div>
  <a class="btn btn-dark" href="#" style="left:824px;top:113px;width:144px;height:34px">Browse All Videos</a>

  <div class="video-thumb" role="img" aria-label="Man and woman in headphones recording a podcast at a bright desk" style="left:268px;top:203px;background:linear-gradient(120deg,#8a8580,#d8d3cc 50%,#bfb5ab)">
    <svg width="66" height="66" viewBox="0 0 66 66"><circle cx="33" cy="33" r="33" fill="#5fd3c6" opacity=".85"/><path d="M26 21l20 12-20 12z" fill="#3e6a66"/></svg>
  </div>
  <h3 class="video-name" style="left:630px;top:222px">Ellis Hartwell</h3>
  <p class="video-copy" style="left:630px;top:260px">We sit down for a candid discussion with depression expert Dr. Ellis Hartwell who helps us shine a spotlight on the culture of…</p>
  <a class="learn-more" href="#" style="left:630px;top:322px">Learn More &gt;&gt;</a>
  <p class="also" style="left:630px;top:357px">Also Available As: <b>Podcast</b></p>
  <div class="divider" style="top:416px"></div>

  <h3 class="video-name" style="left:297px;top:476px">Noel Ashby</h3>
  <p class="video-copy" style="left:297px;top:515px">Talk show host Noel Ashby shares his experience on alcoholism and suicide during his youth.</p>
  <a class="learn-more" href="#" style="left:297px;top:582px">Learn More &gt;&gt;</a>
  <div class="video-thumb" role="img" aria-label="Smiling man at a desk with a laptop in a sunny office" style="left:620px;top:459px;background:linear-gradient(120deg,#b8926a,#e3d6c2 45%,#4b4a4c)">
    <svg width="66" height="66" viewBox="0 0 66 66"><circle cx="33" cy="33" r="33" fill="#5fd3c6" opacity=".85"/><path d="M26 21l20 12-20 12z" fill="#3e6a66"/></svg>
  </div>
  <div class="divider" style="top:673px"></div>

  <div class="video-thumb" role="img" aria-label="Two women in headphones talking at microphones in a blue studio" style="left:268px;top:715px;background:linear-gradient(120deg,#1f4e7a,#3c6f9a 45%,#d9d6d1)">
    <svg width="66" height="66" viewBox="0 0 66 66"><circle cx="33" cy="33" r="33" fill="#5fd3c6" opacity=".85"/><path d="M26 21l20 12-20 12z" fill="#3e6a66"/></svg>
  </div>
  <h3 class="video-name" style="left:630px;top:733px">Vera Lindqvist</h3>
  <p class="video-copy" style="left:630px;top:771px">Today's Talk outtakes with Rosa reads out readers' comments and share their thoughts about cultural percpetion on suicide and…</p>
  <a class="learn-more" href="#" style="left:630px;top:836px">Learn More &gt;&gt;</a>
  <p class="also" style="left:630px;top:871px">Also Available As: <b>Podcast</b></p>
  <div class="divider" style="top:929px"></div>
</section>

<section class="articles">
  <h2 class="section-title">ARTICLES</h2>
  <div class="rule"></div>
  <a class="btn btn-light" href="#" style="left:866px;top:81px;width:102px;height:33px">Visit Blog</a>

  <article class="feature-card">
    <div role="img" aria-label="Two women talking in a bright room with large windows" style="position:absolute;inset:0;background:linear-gradient(160deg,#f2f0ec,#c9c2b8 50%,#5b4a40)"></div>
    <span class="read-time" style="left:11px;top:137px">5 min read</span>
    <div class="feature-overlay">
      <h4 class="feature-title">How Sharing Can Prevent Depression</h4>
      <span class="feature-date">26 Aug 2023</span>
      <p class="feature-copy">Ipsum dolor sit amet, consectetur adipiscing elit, sed do eiusmod tempor incididunt ut labore et dolore magna</p>
    </div>
  </article>

  <article class="side-card" style="top:149px">
    <div class="side-thumb" role="img" aria-label="Young woman holding a book outdoors" style="background:linear-gradient(160deg,#8fa7b2,#3e6f86 60%,#c8b9a6)"></div>
    <span class="read-time" style="left:8px;top:99px">3 min read</span>
    <h4 class="side-title" style="top:14px">Best Podcasts for Spiritual Wellbeing</h4>
    <span class="side-date" style="top:33px">16 Aug 2023</span>
    <p class="side-copy" style="top:50px">Con sectetur adi piscing elit, sed do eiu smod tempor incididunt ut labore et dolore magna aliqua. Quis ipsum sus pendisse ultrices gravida.</p>
  </article>

  <article class="side-card" style="top:283px">
    <div class="side-thumb" role="img" aria-label="Woman with pink hair holding a microphone" style="background:linear-gradient(160deg,#d6c7c6,#b48aa8 50%,#8b6f78)"></div>
    <span class="read-time" style="left:8px;top:99px">12 min read</span>
    <h4 class="side-title" style="top:9px">How To Overcome Depression and Thoughts of Suicide by Dr. Mina Lo</h4>
    <span class="side-date" style="top:44px">11 Aug 2023</span>
    <p class="side-copy" style="top:64px">Dolor sit amet, con sectetur adi piscing elit, sed do eiusmod tempor incididunt ut labore et…</p>
  </article>

  <svg class="carousel-arrow" style="left:531px;top:434px" width="30" height="30" viewBox="0 0 30 30"><circle cx="15" cy="15" r="13.5" fill="none" stroke="#fff" stroke-width="1.2"/><path d="M17 10l-5 5 5 5" fill="none" stroke="#fff" stroke-width="1.3"/></svg>
  <svg class="carousel-arrow" style="left:590px;top:434px" width="30" height="30" viewBox="0 0 30 30"><circle cx="15" cy="15" r="13.5" fill="none" stroke="#fff" stroke-width="1.2"/><path d="M13 10l5 5-5 5" fill="none" stroke="#fff" stroke-width="1.3"/></svg>
</section>

<section class="newsletter">
  <div role="img" aria-label="Soft misty sky over a hillside with a person raising their arms at the summit" style="position:absolute;inset:0;background:linear-gradient(180deg,#f1ece7 0%,#ece2dd 60%,#e2d2cc 100%)"></div>
  <div aria-hidden="true" style="position:absolute;right:0;bottom:0;width:460px;height:150px;background:linear-gradient(160deg,rgba(212,190,182,0) 35%,rgba(190,165,156,.75) 70%,rgba(170,142,134,.9));"></div>
  <h2 class="news-title">SUBSCRIBE TO OUR NEWSLETTER</h2>
  <p class="news-lede">Stay up to date with the best content and podcasts with our newsletter</p>
  <div class="email-field">Email</div>
  <a class="btn btn-dark" href="#">Subscribe</a>
</section>

<section class="contact">
  <div role="img" aria-label="Stack of balanced pebbles on a beach by the sea" style="position:absolute;left:0;top:0;width:556px;height:445px;background:linear-gradient(180deg,#5b6f78 0%,#8aa0a6 35%,#b7aea2 70%,#8f8379 100%)"></div>
  <h2 class="contact-title">CONTACT US</h2>
  <p class="contact-lede">Questions or requests for our next podcasts? We'd love to hear from you. Why not drop us a line?</p>
  <div class="field" style="top:165px;height:30px">Name</div>
  <div class="field" style="top:211px;height:31px">Email address</div>
  <div class="field" style="top:257px;height:96px">Type your message here</div>
  <a class="btn btn-dark" href="#">Send</a>
</section>

<footer class="site-footer">
  <a class="brand" href="#"><span class="brand-dot"></span>Candid Dialogues</a>
  <nav class="footer-nav">
    <a href="#" style="left:400px">Home</a>
    <a href="#" style="left:484px">Podcasts</a>
    <a href="#" style="left:587px">Blog</a>
    <a href="#" style="left:660px">About</a>
    <a href="#" style="left:745px">Contact</a>
  </nav>
  <div class="social"><a href="#">WorkNexo</a><a href="#">Friendloop</a><a href="#">Pictora</a></div>
  <div class="rule"></div>
  <p class="footer-url">www.candiddialogues.org</p>
</footer>

</body>
</html>
```